Influencer agency website

K-Brightcast, Influencer Marketing Agency. A creative space where influencers and brands meet. We represent ideas and collaborations which bring marketing success to companies and brands.
Influencer types: Nano, Micro, Macro
Brand Types: Fashion, Beauty, Luxury Goods, Gaming, Sports, Home & Living, Travel, Lifestyle, Automotive

```html
<!DOCTYPE html>
<html lang="en">
<head>
<meta charset="UTF-8">
<title>K-Brightcast – Influencer Marketing Agency</title>
<link href="https://fonts.googleapis.com/css2?family=Montserrat:wght@400;500;600;700&display=swap" rel="stylesheet">
<style>
:root{
  --ink:#1f1c1c;
  --taupe:#c09e86;
  --taupe-dark:#a08676;
  --cocoa:#6f6462;
  --accent:#b89880;
  --hero-bg:#ddd2c9;
  --cream:#f5f0ed;
  --text:#2b2525;
  --muted:#7a6e6a;
  --white:#ffffff;
}
*{margin:0;padding:0;box-sizing:border-box}
html,body{width:1200px;height:3420px;overflow:hidden}
body{font-family:'Montserrat',sans-serif;color:var(--text);background:var(--white);position:relative}
.abs{position:absolute}
.center{text-align:center}

/* nav */
.site-header{position:absolute;left:0;top:0;width:1200px;height:73px;background:var(--ink);z-index:5}
.brand-badge{position:absolute;left:90px;top:-23px;width:160px;height:160px;border-radius:50%;background:var(--ink);display:flex;align-items:center;justify-content:center;padding-top:30px}
.brand-badge span{color:var(--taupe);font-weight:600;font-size:17px}
.nav-link{position:absolute;top:26px;color:var(--white);font-size:16px;text-decoration:none}
.nav-link.active{color:var(--taupe)}
.btn{position:absolute;display:flex;align-items:center;justify-content:center;color:var(--white);background:linear-gradient(90deg,#a88c78,#c7ad99);border-radius:6px;font-size:17px;font-weight:500}

/* hero */
.hero{position:absolute;left:0;top:73px;width:1200px;height:515px;background:var(--hero-bg);overflow:hidden}
.hero-photo{position:absolute;left:0;top:0;width:780px;height:515px;background:linear-gradient(90deg,#cfc1b3 0%,#bba999 45%,#d5c9bd 80%,rgba(221,210,201,0) 100%)}
.hero-kicker{position:absolute;left:700px;width:400px;top:152px;font-size:50px;color:#6e625d;text-align:center}
.hero-title{position:absolute;left:680px;width:440px;top:210px;font-size:64px;font-weight:700;color:#6e625d;text-align:center}

/* section headings */
.ghost{position:absolute;left:0;width:1200px;text-align:center;font-weight:500;color:transparent;-webkit-text-stroke:1.5px #e7e1dd;white-space:nowrap;line-height:1}
.section-title{position:absolute;left:0;width:1200px;text-align:center;font-weight:700;color:var(--accent);line-height:1}

/* why us */
.feature-icon{position:absolute;width:138px;height:138px;border-radius:50%;background:radial-gradient(circle at 40% 35%,#6f6462 55%,#a08676 100%);display:flex;align-items:center;justify-content:center}
.feature-title{position:absolute;width:340px;font-size:21px;font-weight:600;text-align:center;color:var(--text)}
.feature-copy{position:absolute;width:320px;font-size:20px;line-height:30px;text-align:center;color:#3a3232}

/* about */
.about{position:absolute;left:0;top:1290px;width:1200px;height:560px;background:var(--taupe)}
.about .ghost{-webkit-text-stroke:1.5px rgba(255,255,255,.45)}
.about-lead{position:absolute;left:113px;top:242px;width:520px;font-size:19px;line-height:30px;font-weight:600;color:var(--white)}
.about-copy{position:absolute;left:111px;top:310px;width:515px;font-size:18.5px;line-height:30px;color:var(--white)}
.about-photo{position:absolute;left:717px;top:1506px;width:305px;height:398px;border-radius:30px;background:linear-gradient(160deg,#f3f1ef 0%,#5a6b86 55%,#2b2f33 100%);z-index:2}

/* influencer types */
.type-circle{position:absolute;width:366px;height:366px;border-radius:50%;color:var(--white);text-align:center;padding:90px 60px 0}
.type-circle h3{font-size:22px;font-weight:500;margin-bottom:16px}
.type-circle p{font-size:18.5px;line-height:28px}
.type-nano{background:var(--taupe)}
.type-micro{background:rgba(140,112,96,.82)}
.type-macro{background:rgba(95,84,82,.92)}

/* brand types */
.brands{position:absolute;left:0;top:2539px;width:1200px;height:630px;background:var(--cream)}
.brand-photo{position:absolute;width:194px;height:194px;border-radius:50%}
.brand-label{position:absolute;width:220px;text-align:center;font-size:21px;font-weight:500;color:var(--muted);letter-spacing:.5px}
.arrow{position:absolute}

/* footer */
.site-footer{position:absolute;left:0;top:3169px;width:1200px;height:251px;background:var(--ink);color:var(--white)}
.footer-brand{position:absolute;left:0;width:1200px;top:74px;text-align:center;color:var(--taupe);font-weight:600;font-size:22px}
.footer-link{position:absolute;top:167px;font-size:16px;color:var(--white)}
.copyright{position:absolute;left:0;width:1200px;top:210px;text-align:center;font-size:16px}
</style>
</head>
<body>

<header class="site-header">
  <div class="brand-badge"><span>K-Brightcast</span></div>
  <a class="nav-link active" style="left:451px">Home</a>
  <a class="nav-link" style="left:523px">Our Work</a>
  <a class="nav-link" style="left:618px">Resources</a>
  <a class="nav-link" style="left:725px">Influencers</a>
  <a class="nav-link" style="left:836px">About Us</a>
  <div class="btn" style="left:946px;top:16px;width:142px;height:42px">Contact Us</div>
</header>

<section class="hero">
  <div class="hero-photo" role="img" aria-label="Smiling woman seated on a sofa recording herself with a camera on a tripod"></div>
  <div class="hero-kicker">Welcome to</div>
  <div class="hero-title">K-Brightcast</div>
  <div class="btn" style="left:825px;top:304px;width:142px;height:42px">Get Started</div>
</section>

<!-- why us -->
<div class="ghost" style="top:630px;font-size:135px">Why Us</div>
<div class="section-title" style="top:686px;font-size:45px">Why Us</div>

<div class="feature-icon" style="left:171px;top:808px">
  <svg width="72" height="72" viewBox="0 0 72 72" fill="none" stroke="#fff" stroke-width="2.2" stroke-linecap="round" stroke-linejoin="round"><rect x="22" y="10" width="26" height="48" rx="4"/><line x1="31" y1="52" x2="39" y2="52"/><path d="M50 12l2.5 5 5.5.8-4 3.9 1 5.5-5-2.6-5 2.6 1-5.5-4-3.9 5.5-.8z"/><line x1="8" y1="24" x2="18" y2="24"/><line x1="10" y1="30" x2="18" y2="30"/></svg>
</div>
<div class="feature-icon" style="left:531px;top:808px">
  <svg width="72" height="72" viewBox="0 0 72 72" fill="none" stroke="#fff" stroke-width="2.2" stroke-linecap="round" stroke-linejoin="round"><rect x="22" y="10" width="26" height="48" rx="4"/><line x1="31" y1="52" x2="39" y2="52"/><circle cx="35" cy="28" r="7"/><path d="M50 12l2.5 5 5.5.8-4 3.9 1 5.5-5-2.6-5 2.6 1-5.5-4-3.9 5.5-.8z"/><line x1="8" y1="24" x2="18" y2="24"/><line x1="10" y1="30" x2="18" y2="30"/></svg>
</div>
<div class="feature-icon" style="left:889px;top:808px">
  <svg width="72" height="72" viewBox="0 0 72 72" fill="none" stroke="#fff" stroke-width="2.2" stroke-linecap="round"><circle cx="36" cy="36" r="6"/><circle cx="36" cy="10" r="4"/><circle cx="36" cy="62" r="4"/><circle cx="10" cy="36" r="4"/><circle cx="62" cy="36" r="4"/><circle cx="17" cy="17" r="4"/><circle cx="55" cy="17" r="4"/><circle cx="17" cy="55" r="4"/><circle cx="55" cy="55" r="4"/><path d="M36 14v16M36 42v16M14 36h16M42 36h16M20 20l11 11M52 20L41 31M20 52l11-11M52 52L41 41"/></svg>
</div>

<div class="feature-title" style="left:70px;top:993px">Data-Powered Strategy</div>
<div class="feature-title" style="left:430px;top:993px">Biggest Network</div>
<div class="feature-title" style="left:788px;top:993px">Flawless Execution</div>
<p class="feature-copy" style="left:80px;top:1032px">Lorem ipsum dolo sit amet, consectetur adipiscing elit, sed do eiusmod tempor inc ididunt ut labore et dolore magna aliqua.</p>
<p class="feature-copy" style="left:440px;top:1032px">Lorem ipsum dolo sit amet, consectetur adipiscing elit, sed do eiusmod tempor inc ididunt ut labore et dolore magna aliqua.</p>
<p class="feature-copy" style="left:798px;top:1032px">Lorem ipsum dolo sit amet, consectetur adipiscing elit, sed do eiusmod tempor inc ididunt ut labore et dolore magna aliqua.</p>

<!-- about -->
<section class="about">
  <div class="ghost" style="top:55px;font-size:145px">About Us</div>
  <div class="section-title" style="top:95px;font-size:48px;color:var(--white)">About Us</div>
  <p class="about-lead">Perspiciatis unde omnis istnatus error olum accusanti veritatis et quch beatae.</p>
  <p class="about-copy">Sed ut perspiciatis unde omnis iste natus error oluptatem accusantium doloremque laudantium, totam rem aperiam, eaque ipsa quae ab illo inventore veritatis et quch beatae vitae dicta sunt explicabo. Nemo eni voluptatem voluptas sit aspernatur aut odit aut fugit, uia consequuntur magni dolores eos qui ratione voluptatem sequi nesciunt. Neque porro quisquam est.</p>
</section>
<div class="about-photo" role="img" aria-label="Excited young woman with a backpack calling out as she leans out of a smartphone screen"></div>

<!-- influencer types -->
<div class="ghost" style="top:1908px;font-size:140px">Influencer</div>
<div class="section-title" style="top:1940px;font-size:46px">Influencer Types</div>

<div class="type-circle type-nano" style="left:112px;top:2089px"><h3>Nano</h3><p>Lorem ipsum dolor amet, consectetur adipiscig elit, sed do eiusmor incididunt ut labore et dolore magna aliqua.</p></div>
<div class="type-circle type-micro" style="left:417px;top:2089px"><h3>Micro</h3><p>Lorem ipsum dolor amet, consectetur adipiscig elit, sed do eiusmor incididunt ut labore et dolore magna aliqua.</p></div>
<div class="type-circle type-macro" style="left:721px;top:2089px"><h3>Macro</h3><p>Lorem ipsum dolor amet, consectetur adipiscig elit, sed do eiusmor incididunt ut labore et dolore magna aliqua.</p></div>

<!-- brand types -->
<section class="brands">
  <div class="ghost" style="top:83px;font-size:145px">Brand Types</div>
  <div class="section-title" style="top:126px;font-size:48px">Brand Types</div>

  <svg class="arrow" style="left:42px;top:394px" width="28" height="20" viewBox="0 0 28 20" fill="none" stroke="#b7aaa3" stroke-width="2" stroke-linecap="round" stroke-linejoin="round"><path d="M26 10H3M10 3L3 10l7 7"/></svg>
  <svg class="arrow" style="left:1132px;top:394px" width="28" height="20" viewBox="0 0 28 20" fill="none" stroke="#4a4141" stroke-width="2" stroke-linecap="round" stroke-linejoin="round"><path d="M2 10h23M18 3l7 7-7 7"/></svg>

  <div class="brand-photo" style="left:111px;top:313px;background:linear-gradient(160deg,#8a8f6e,#e6c4c8)" role="img" aria-label="Fashion model in a pink outfit"></div>
  <div class="brand-photo" style="left:373px;top:313px;background:linear-gradient(160deg,#8fae55,#3c4a6a)" role="img" aria-label="Man playing pickleball outdoors"></div>
  <div class="brand-photo" style="left:634px;top:313px;background:linear-gradient(180deg,#6a9bc4,#a0654d)" role="img" aria-label="Traveller in a sun hat with a backpack overlooking the sea"></div>
  <div class="brand-photo" style="left:894px;top:313px;background:linear-gradient(160deg,#e7e2de,#d9b59c)" role="img" aria-label="Woman with glowing skin posing for a beauty shot"></div>

  <div class="brand-label" style="left:98px;top:528px">Fashion</div>
  <div class="brand-label" style="left:360px;top:528px">Sports</div>
  <div class="brand-label" style="left:621px;top:528px">Travel</div>
  <div class="brand-label" style="left:881px;top:528px">Beauty</div>
</section>

<footer class="site-footer">
  <div class="footer-brand">K-Brightcast</div>
  <span class="footer-link" style="left:328px">Home</span>
  <span class="footer-link" style="left:398px">Our Work</span>
  <span class="footer-link" style="left:493px">Resources</span>
  <span class="footer-link" style="left:600px">Influencers</span>
  <span class="footer-link" style="left:712px">About Us</span>
  <span class="footer-link" style="left:809px">Contact</span>
  <div class="copyright">2023 K-Brightcast. All Rights Reserved.</div>
</footer>

</body>
</html>
```